Brackenfold Latches Business Cards

Need high quality business card designed around my company logo. Ideally the cards need to be a glossy black as the logo goes well with a black background.

The company is a Locksmithing business.

Domestic clients are Residential Home Owners and Landlords. Commercial clients are local businesses, estate agents, landlords, solicitors

Services offered :
Emergency Lock Out
New Lock Fitting & Replacement
High Security Upgrades
UPVC lock repairs
Mobile Key Cutting
Free Security Reviews

Qualificatons & Certifications:
Accredited Guild & Tower KSR Level 3, QTRB
Fully Insured
PVX Checked

Contact & Business Details:

Business Name : Brackenfold Latches
Name: Rob Fenwick
Tel: 01823 574419 Office / 07841592637 Mobile
Email: contact@brackenfoldlatches.com
Website: www.brackenfoldlatches.com

(please note that the website is currently under development and not available to view)

Locksmith

Name: Rob Fenwick

Services:
Emergency Lock Out
High Security Upgrades
UPVC lock repairs
Mobile Key Cutting
Free Security Reviews

• Ideally the cards should be a glossy black as the logo stands out better on a black background.

Logo on front and the word LOCKSMITH should be incorporated into the front design of the card.

Qualifications & Certifications on the back ideally along the top / bottom of the card or split (I.e along the top “ Accredited : Guild & Tower Level 3 , QTRB”
and along the bottom , “Fully Insured & PVX Checked”

Services offered ideally listed on the back of the card, preferably split into two columns. If possible the logo could also be incorporated onto the back of the card between the two services columns (I.e the services listed either side of the logo)
• On the back of the card, have the logo in the middle with the services listed either side of the logo I.e 3 services on left of logo and three to the right.

```html
<!DOCTYPE html>
<html lang="en">
<head>
<meta charset="utf-8">
<title>Brackenfold Latches Business Cards</title>
<link rel="stylesheet" href="https://fonts.googleapis.com/css2?family=Cinzel:wght@500;700&family=Playfair+Display:wght@700&family=Lora:wght@500&display=swap">
<style>
  :root {
    --page-bg: #161616;
    --card-bg: #2a2a2a;
    --card-edge: #1e1e1e;
    --gold: #d9a92e;
    --gold-light: #f3d77a;
    --gold-deep: #9c6d12;
  }
  * { box-sizing: border-box; margin: 0; padding: 0; }
  html, body { width: 1200px; height: 1108px; overflow: hidden; background: var(--page-bg); }
  .canvas {
    position: relative; width: 1200px; height: 1108px;
    display: flex; justify-content: center; align-items: center; gap: 80px;
  }
  .card {
    position: relative; width: 440px; height: 760px;
    background: var(--card-bg); border-radius: 34px;
    box-shadow: 0 6px 0 var(--card-edge), 0 12px 0 #181818, 0 24px 40px rgba(0,0,0,.6);
    color: var(--gold); text-align: center;
  }
  /* Front */
  .brand {
    position: absolute; top: 150px; left: 0; right: 0;
    display: flex; flex-direction: column; align-items: center; gap: 18px;
  }
  .brand-dot { width: 26px; height: 26px; border-radius: 50%; background: var(--gold); }
  .brand-name {
    font-family: "Cinzel", serif; font-weight: 700; font-size: 40px;
    line-height: 1.15; letter-spacing: 2px; color: var(--gold);
  }
  .services { position: absolute; top: 430px; left: 0; right: 0; font-family: "Cinzel", serif; }
  .services-title { font-weight: 700; font-size: 19px; letter-spacing: 10px; margin-bottom: 26px; }
  .services-list { list-style: none; font-weight: 500; font-size: 13.5px; letter-spacing: 4px; line-height: 1.75; }
  .services-list .gap { height: 20px; }
  /* Back */
  .person { position: absolute; top: 110px; left: 0; right: 0; }
  .person-name { font-family: "Playfair Display", serif; font-weight: 700; font-size: 42px; letter-spacing: 4px; }
  .person-role { font-family: "Lora", serif; font-size: 17px; letter-spacing: 9px; margin-top: 8px; }
  .contact-icons { position: absolute; top: 380px; left: 0; right: 0; display: flex; justify-content: center; gap: 22px; }
  .contact-icons svg { width: 30px; height: 30px; fill: var(--gold); }
  .contact-list {
    position: absolute; top: 440px; left: 0; right: 0; list-style: none;
    font-family: "Lora", serif; font-size: 15.5px; letter-spacing: 2px; line-height: 1.75;
  }
  .crest-art {
    position: absolute; top: 560px; left: 110px; width: 220px; height: 110px;
    border-radius: 0 0 110px 110px;
    background: radial-gradient(ellipse at 50% 40%, var(--gold-light), var(--gold) 45%, var(--gold-deep) 100%);
    opacity: .85;
  }
  .accreditation {
    position: absolute; bottom: 42px; left: 0; right: 0;
    font-family: "Lora", serif; font-size: 12.5px; letter-spacing: 3px; line-height: 1.6;
  }
</style>
</head>
<body>
<main class="canvas">
  <section class="card card-front">
    <div class="brand">
      <span class="brand-dot"></span>
      <h1 class="brand-name">BRACKENFOLD<br>LATCHES</h1>
    </div>
    <div class="services">
      <h2 class="services-title">SERVICES OFFERED</h2>
      <ul class="services-list">
        <li>EMERGENCY LOCK OUT</li>
        <li>HIGH SECURITY UPGRADES</li>
        <li>UPVC LOCK REPAIRS</li>
        <li class="gap"></li>
        <li>MOBILE KEY CUTTING</li>
        <li>NEW LOCK FITTING &amp; REPLACEMENT</li>
        <li>FREE SECURITY REVIEWS</li>
      </ul>
    </div>
  </section>

  <section class="card card-back">
    <div class="person">
      <h2 class="person-name">Rob Fenwick</h2>
      <p class="person-role">Director</p>
    </div>
    <div class="contact-icons">
      <svg viewBox="0 0 24 24" aria-label="Office phone"><path d="M6.6 2.5c.6-.4 1.4-.2 1.8.4l2 3.2c.3.6.2 1.3-.3 1.7L8.6 9c.9 2.4 2.9 4.8 5.4 6.1l1.3-1.5c.4-.5 1.1-.6 1.7-.3l3.3 1.8c.6.3.9 1.1.5 1.7l-1.2 2.3c-.5.9-1.6 1.4-2.6 1.1C10 18.4 5 12.8 3.7 6.4c-.2-1 .2-2 1-2.6z"/></svg>
      <svg viewBox="0 0 24 24" aria-label="Mobile phone"><path d="M6.6 2.5c.6-.4 1.4-.2 1.8.4l2 3.2c.3.6.2 1.3-.3 1.7L8.6 9c.9 2.4 2.9 4.8 5.4 6.1l1.3-1.5c.4-.5 1.1-.6 1.7-.3l3.3 1.8c.6.3.9 1.1.5 1.7l-1.2 2.3c-.5.9-1.6 1.4-2.6 1.1C10 18.4 5 12.8 3.7 6.4c-.2-1 .2-2 1-2.6z"/></svg>
      <svg viewBox="0 0 24 24" aria-label="Email"><path d="M2 5h20v14H2z M3.5 6.5 12 13l8.5-6.5" stroke="#2a2a2a" stroke-width="1.2"/></svg>
      <svg viewBox="0 0 24 24" aria-label="Website"><circle cx="12" cy="12" r="10"/><path d="M2 12h20M12 2c3 3 3 17 0 20M12 2c-3 3-3 17 0 20M4 7h16M4 17h16" stroke="#2a2a2a" stroke-width="1.2" fill="none"/></svg>
    </div>
    <ul class="contact-list">
      <li>01823 574419</li>
      <li>07841592637</li>
      <li>contact@brackenfoldlatches.com</li>
      <li>www.brackenfoldlatches.com</li>
    </ul>
    <div class="crest-art" role="img" aria-label="Gold laurel wreath ornament with padlocks and stars"></div>
    <p class="accreditation">Accredited Guild &amp; Tower KSR Level 3,<br>QTRB-Fully Insured PVX Checked.</p>
  </section>
</main>
</body>
</html>
```